Copper Ridge Business Cards For New Startup

I am looking for you to design some business cards for a new startup https://copperridgehub.example. I have supplied logo, brand guidelines and our signatures as a guide.

We need this to reflect the brand guidelines and the website for brand consistency,

What is Copper Ridge?

Mallorca's Business Growth Community
Join your new business community full of passionate entrepreneurs who
love to solve problems and help each other grow together!

Any questions you can ask.

Target Market(s)

Business to Business

Contact Information for Business Card

These are attached (signatures) to the job

Font styles to use
Other font styles liked:
• Open Sans

Requirements
Must have
• Match design guidelines
Nice to have
• Photos of our faces so people remember us

```html
<!DOCTYPE html>
<html lang="en">
<head>
<meta charset="utf-8">
<title>Copper Ridge – Business Cards</title>
<link href="https://fonts.googleapis.com/css2?family=Open+Sans:wght@400;600;700&display=swap" rel="stylesheet">
<style>
  :root {
    --olive: #68692e;
    --white: #ffffff;
    --paper: #f3f3f1;
    --ink: #555555;
  }
  * { box-sizing: border-box; margin: 0; padding: 0; }
  html, body {
    width: 1200px; height: 900px; overflow: hidden;
    background: var(--paper);
    font-family: "Open Sans", Arial, sans-serif;
  }
  .canvas { position: relative; width: 1200px; height: 900px; }
  .card { position: absolute; top: 97px; width: 403px; height: 706px; }

  /* Front */
  .card-front { left: 130px; background: var(--olive); color: var(--white); }
  .front-brand {
    position: absolute; top: 364px; left: 0; width: 100%;
    display: flex; flex-direction: column; align-items: center;
  }
  .brand-mark {
    width: 84px; height: 84px; border-radius: 50%;
    border: 3px solid currentColor;
  }
  .front-name {
    margin-top: 12px; font-size: 38px; font-weight: 600;
    letter-spacing: 0.5px; line-height: 1.1;
  }
  .front-url { margin-top: 4px; font-size: 19px; line-height: 1.2; }
  .social-row { margin-top: 14px; display: flex; gap: 17px; }
  .social-dot { width: 18px; height: 18px; border-radius: 50%; background: var(--white); }
  .front-strip {
    position: absolute; left: 25px; right: 25px; bottom: 0; height: 10px;
    background: var(--white);
  }

  /* Back */
  .card-back { left: 668px; background: var(--white); color: var(--ink); }
  .back-brand {
    position: absolute; top: 31px; left: 0; width: 100%;
    display: flex; align-items: center; justify-content: center; gap: 14px;
    color: var(--olive);
  }
  .back-brand .brand-mark { width: 64px; height: 64px; border-width: 3px; }
  .back-name { font-size: 30px; font-weight: 600; line-height: 1.1; letter-spacing: 0.3px; }
  .back-url { font-size: 16px; line-height: 1.2; color: var(--olive); }

  .person { position: absolute; width: 330px; }
  .person-left { top: 162px; left: 40px; }
  .person-right { top: 423px; right: 42px; text-align: right; }
  .portrait {
    width: 100px; height: 100px; border: 2px solid var(--olive); border-radius: 5px;
    display: inline-block;
  }
  .portrait-a { background: linear-gradient(160deg, #c9c2b6, #6f7f95); }
  .portrait-b { background: linear-gradient(160deg, #d8cdb9, #c99d7e); }
  .person-name { margin-top: 15px; font-size: 19px; font-weight: 700; color: var(--olive); line-height: 1.2; }
  .person-role { font-size: 16px; line-height: 1.3; }
  .contact { list-style: none; margin-top: 10px; font-size: 17.5px; line-height: 26px; }
  .contact li { display: flex; align-items: center; gap: 8px; }
  .person-right .contact li { justify-content: flex-end; }
  .icon { width: 18px; height: 18px; fill: var(--olive); flex: none; }
  .back-strip {
    position: absolute; left: 25px; right: 25px; bottom: 0; height: 10px;
    background: var(--olive);
  }
</style>
</head>
<body>
<main class="canvas">

  <section class="card card-front" aria-label="Card front">
    <div class="front-brand">
      <span class="brand-mark" aria-hidden="true"></span>
      <h1 class="front-name">COPPER RIDGE</h1>
      <p class="front-url">copperridgehub.example</p>
      <ul class="social-row" aria-label="Social channels" style="list-style:none">
        <li class="social-dot"></li><li class="social-dot"></li><li class="social-dot"></li><li class="social-dot"></li><li class="social-dot"></li>
      </ul>
    </div>
    <div class="front-strip"></div>
  </section>

  <section class="card card-back" aria-label="Card back">
    <header class="back-brand">
      <span class="brand-mark" aria-hidden="true"></span>
      <div>
        <h2 class="back-name">COPPER RIDGE</h2>
        <p class="back-url">copperridgehub.example</p>
      </div>
    </header>

    <article class="person person-left">
      <div class="portrait portrait-a" role="img" aria-label="Portrait photo of Daniel Ferrer"></div>
      <h3 class="person-name">Daniel Ferrer</h3>
      <p class="person-role">Founder &amp; Growth Hacker</p>
      <ul class="contact">
        <li><svg class="icon" viewBox="0 0 24 24"><path d="M6.6 10.8a15.1 15.1 0 0 0 6.6 6.6l2.2-2.2a1 1 0 0 1 1-.25 11.4 11.4 0 0 0 3.6.57 1 1 0 0 1 1 1V20a1 1 0 0 1-1 1A17 17 0 0 1 3 4a1 1 0 0 1 1-1h3.5a1 1 0 0 1 1 1c0 1.25.2 2.45.57 3.57a1 1 0 0 1-.25 1z"/></svg>+ 34 600 482 915</li>
        <li><svg class="icon" viewBox="0 0 24 24"><path d="M2 5h20v2.2l-10 6.3L2 7.2z M2 9.5l10 6.3 10-6.3V19H2z"/></svg>df@copperridgehub.example</li>
      </ul>
    </article>

    <article class="person person-right">
      <div class="portrait portrait-b" role="img" aria-label="Portrait photo of Laura Whitfield"></div>
      <h3 class="person-name">Laura Whitfield</h3>
      <p class="person-role">Relationship Director</p>
      <ul class="contact">
        <li>+ 44 7700 900 458<svg class="icon" viewBox="0 0 24 24"><path d="M6.6 10.8a15.1 15.1 0 0 0 6.6 6.6l2.2-2.2a1 1 0 0 1 1-.25 11.4 11.4 0 0 0 3.6.57 1 1 0 0 1 1 1V20a1 1 0 0 1-1 1A17 17 0 0 1 3 4a1 1 0 0 1 1-1h3.5a1 1 0 0 1 1 1c0 1.25.2 2.45.57 3.57a1 1 0 0 1-.25 1z"/></svg></li>
        <li>lw@copperridgehub.example<svg class="icon" viewBox="0 0 24 24"><path d="M2 5h20v2.2l-10 6.3L2 7.2z M2 9.5l10 6.3 10-6.3V19H2z"/></svg></li>
      </ul>
    </article>

    <div class="back-strip"></div>
  </section>

</main>
</body>
</html>
```